Velisto Events Business Card

We need a business cards that stands out to our clients. We are company who targets prestige clients to spend money with us on experiences, so our image needs to be prestige
Target Market(s)
Corporate
Contact Information for Business Card
There will be four different names on the business cards
Dana Morrowby
Director
O: 02 5147 3086
M: 0451 692 038
E: info@velistoevents.example.au
Facebook: @velistoevents
Instagram: velistoevents
www.velistoevents.example.au
Nathaniel Morrowby
Director
O: 02 5147 3086
M: 0467 215 904
Facebook: @velistoevents
Instagram: velistoevents
www.velistoevents.example.au
Teodor Vinkel
Director
O: 02 5147 3086
M: 0478 903 527
Facebook: @velistoevents
Instagram: velistoevents
www.velistoevents.example.au
Mabel Hartung
Director
O: 02 5147 3086
Facebook: @velistoevents
Instagram: velistoevents
www.velistoevents.example.au
Colors
Designer to choose colors to be used in the design.
Look and feel

```html
<!DOCTYPE html>
<html lang="en">
<head>
<meta charset="utf-8">
<title>Velisto Events – Business Card</title>
<link rel="stylesheet" href="https://fonts.googleapis.com/css2?family=Inter:wght@300;400&display=swap">
<style>
  :root {
    --navy: #262350;
    --gold: #c9a24a;
    --paper: #ffffff;
    --page: #ffffff;
  }
  * { margin: 0; padding: 0; box-sizing: border-box; }
  html, body {
    width: 960px; height: 1200px; overflow: hidden;
    background: var(--page);
    font-family: "Inter", "Helvetica Neue", Arial, sans-serif;
    color: var(--navy);
  }
  .canvas { position: relative; width: 960px; height: 1200px; }
  .card {
    position: absolute; left: 60px; width: 839px; height: 481px;
  }
  .card--front { top: 80px; background: var(--paper); box-shadow: 0 0 0 1px #eeeef2; }
  .card--back { top: 638px; background: var(--navy); }

  .holder { position: absolute; top: 128px; left: 0; width: 100%; text-align: center; }
  .holder__name { font-weight: 300; font-size: 38px; line-height: 1; letter-spacing: 0.2px; }
  .holder__role { margin-top: 6px; font-weight: 300; font-size: 16px; letter-spacing: 0.5px; }

  .divider { position: absolute; left: 226px; top: 242px; width: 388px; height: 8px; }

  .contact-row {
    position: absolute; left: 0; width: 100%;
    font-weight: 300; font-size: 16px; line-height: 20px; white-space: nowrap;
  }
  .contact-row--address { top: 299px; }
  .contact-row--lines { top: 334px; }
  .contact-item { position: absolute; display: flex; align-items: center; gap: 18px; }
  .contact-item svg { width: 19px; height: 19px; flex: none; }

  .brand {
    position: absolute; left: 0; top: 0; width: 100%; height: 100%;
    display: flex; flex-direction: column; align-items: center; justify-content: center;
    color: var(--gold); font-weight: 400; text-transform: uppercase;
  }
  .brand__mark { width: 22px; height: 22px; background: var(--gold); margin-bottom: 28px; }
  .brand__name { font-size: 40px; letter-spacing: 14px; padding-left: 14px; line-height: 1; }
  .brand__sub { margin-top: 14px; font-size: 17px; letter-spacing: 8px; padding-left: 8px; }
</style>
</head>
<body>
<main class="canvas">

  <section class="card card--front">
    <div class="holder">
      <h1 class="holder__name">Your Name</h1>
      <p class="holder__role">FOUNDER</p>
    </div>

    <svg class="divider" viewBox="0 0 388 8" preserveAspectRatio="none" aria-hidden="true">
      <path d="M0 4 Q194 -1 388 4 Q194 9 0 4 Z" fill="var(--navy)"/>
    </svg>

    <div class="contact-row contact-row--address">
      <div class="contact-item" style="left:280px;">
        <svg viewBox="0 0 20 20" aria-hidden="true">
          <rect width="20" height="20" fill="var(--navy)"/>
          <path d="M10 4 L16 9.5 H14.2 V16 H11.5 V12 H8.5 V16 H5.8 V9.5 H4 Z" fill="#fff"/>
        </svg>
        <span>YOUR ADDRESS COMES HERE</span>
      </div>
    </div>

    <div class="contact-row contact-row--lines">
      <div class="contact-item" style="left:116px;">
        <svg viewBox="0 0 20 20" aria-hidden="true">
          <rect width="20" height="20" fill="var(--navy)"/>
          <path d="M6 4.5 L8.3 4.5 L9.2 7.6 L7.8 8.8 Q9 11.4 11.2 12.3 L12.4 10.9 L15.5 11.8 L15.5 14.1 Q14.8 15.6 13 15.4 Q6.2 14.4 4.6 7 Q4.5 5.2 6 4.5 Z" fill="#fff"/>
        </svg>
        <span>+000 000 000</span>
      </div>
      <div class="contact-item" style="left:294px;">
        <svg viewBox="0 0 20 20" aria-hidden="true">
          <rect width="20" height="20" fill="var(--navy)"/>
          <rect x="6" y="3.5" width="8" height="13" rx="1.2" fill="#fff"/>
          <rect x="7.3" y="5.2" width="5.4" height="8.3" fill="var(--navy)"/>
          <circle cx="10" cy="15" r="0.8" fill="var(--navy)"/>
        </svg>
        <span>+000 000 000</span>
      </div>
      <div class="contact-item" style="left:470px;">
        <svg viewBox="0 0 20 20" aria-hidden="true">
          <rect width="20" height="20" fill="var(--navy)"/>
          <rect x="3.5" y="5.5" width="13" height="9" fill="#fff"/>
          <path d="M3.5 5.5 L10 10.5 L16.5 5.5 M3.5 14.5 L8.3 9.3 M16.5 14.5 L11.7 9.3" stroke="var(--navy)" stroke-width="1.1" fill="none"/>
        </svg>
        <span>info@velistoevents.example.au</span>
      </div>
    </div>
  </section>

  <section class="card card--back">
    <div class="brand">
      <span class="brand__mark" aria-hidden="true"></span>
      <span class="brand__name">Velisto</span>
      <span class="brand__sub">Events</span>
    </div>
  </section>

</main>
</body>
</html>
```